Packaging design for HOT NEW RETAIL BEARD OIL BRAND - Merrow Dalton Apothecary

Packaging design for beard oils. I've attached a brief, and I've also attached a few examples of bottles and boxes. Of course, we need an entirely unique look. I've attached the photo of Merrow Dalton as well - you can choose to use it or not (I'm open).

This product will be sold at national retailers and needs to look like a brand that is sold at boutique

What the consumer wants to see on the shelf:
-Box should larger than others and be soft touch (feels luxurious)
-More “hipster look/feel”
-Text should stand out like inspiration photos - jumping off the shelf to the consumer
-Use the existing logo of Merrow Dalton
-Deco will be wrap label as shown in current product image
-Sample text to pull copy for outer carton (taken from label on glass bottle):
-Strengthen and condition your beard with this blend of natural oils. Sunflower oil is rich in omega, fatty acids and vitamins E, C, B, and A, while avocado oil hydrates the beard fibers from root to tip, keep the beard looking and feeling extraordinary. Smooth into your beard for a healthy sheen and a woodsy scent evoking the great outdoors.
-Cool/Hipster product at discount pricing

Target Market(s)

Men from ages 20-40. Women also buy this product for their men, so it needs to look like a well known brand.

Industry/Entity Type

Hair And Beauty

Font styles to use
Sans Serif

Colors

Designer to choose colors to be used in the design.

Requirements
Must have
• A full label and box design with key call outs:
• Features and benefits - found in attached brief
• Description of what it is: Beard Oil
• Name of frangrance: Sandalwood
• Size: 2 oz / 60 ml
Nice to have
• Feel free to revamp the logo if needed. I am not married to the font for Merrow Dalton Apothecary.

```html
<!DOCTYPE html>
<html lang="en">
<head>
<meta charset="utf-8">
<title>Merrow Dalton Apothecary – Softening Beard Oil Carton &amp; Label Dieline</title>
<link rel="stylesheet" href="https://fonts.googleapis.com/css2?family=Bebas+Neue&family=Oswald:wght@400;500&family=Crimson+Text&family=Source+Sans+3:wght@400&display=swap">
<style>
  :root{
    --ink:#000;
    --paper:#fff;
    --cream:#eeebe3;
    --gold:#a8913f;
    --gold-dark:#4a3f1a;
    --rule:#555;
    --muted:#9a9a9a;
    --label-stripe:#3a4048;
  }
  html,body{margin:0;padding:0;width:1200px;height:848px;overflow:hidden;background:var(--paper);}
  .dieline{display:block;width:1200px;height:848px;}
  .panel{fill:var(--ink);}
  .fold{stroke:var(--rule);stroke-width:3;fill:none;}
  .frame{fill:none;stroke:var(--paper);stroke-width:3;}
  .frame-dash{fill:none;stroke:var(--paper);stroke-width:1.5;stroke-dasharray:7 5;}
  .frame-ink{fill:none;stroke:var(--ink);stroke-width:3;}
  .dots{stroke:var(--paper);stroke-width:2;stroke-dasharray:2 10;stroke-linecap:round;}
  .cream{fill:var(--cream);}
  .gold-band{fill:var(--gold);}
  .brand-seal{fill:var(--ink);stroke:var(--paper);stroke-width:2;}
  .seal-name{font-family:"Oswald",sans-serif;font-weight:500;fill:var(--paper);text-anchor:middle;letter-spacing:1px;}
  .head{font-family:"Bebas Neue","Oswald",sans-serif;fill:var(--paper);text-anchor:middle;}
  .head-ink{font-family:"Bebas Neue","Oswald",sans-serif;fill:var(--ink);text-anchor:middle;}
  .cond{font-family:"Oswald",sans-serif;fill:var(--paper);text-anchor:middle;font-weight:400;}
  .serif{font-family:"Crimson Text",serif;fill:var(--paper);text-anchor:middle;}
  .serif-ink{font-family:"Crimson Text",serif;fill:var(--ink);text-anchor:middle;}
  .serif-left{font-family:"Crimson Text",serif;fill:var(--paper);}
  .volume{font-family:"Source Sans 3",sans-serif;fill:var(--muted);text-anchor:middle;}
  .dim-line{stroke:var(--ink);stroke-width:3;fill:none;}
  .dim-text{font-family:"Source Sans 3",sans-serif;fill:var(--ink);font-size:38px;text-anchor:middle;}
  .note{font-family:"Source Sans 3",sans-serif;fill:var(--ink);font-size:36px;}
</style>
</head>
<body>
<svg class="dieline" viewBox="0 0 2270 1604" xmlns="http://www.w3.org/2000/svg">
  <defs>
    <linearGradient id="gold-wash" x1="0" y1="0" x2="0" y2="1">
      <stop offset="0" stop-color="#000"/>
      <stop offset="1" stop-color="#6b5a22"/>
    </linearGradient>
    <linearGradient id="stripe-wash" x1="0" y1="0" x2="1" y2="1">
      <stop offset="0" stop-color="#2a2f36"/>
      <stop offset="1" stop-color="#4b525c"/>
    </linearGradient>

    <!-- Front face artwork, reused on both front panels -->
    <g id="front-face">
      <rect class="frame" x="150" y="748" width="294" height="488"/>
      <rect class="frame-dash" x="163" y="762" width="268" height="460"/>
      <circle class="brand-seal" cx="297" cy="752" r="62"/>
      <text class="seal-name" x="297" y="748" font-size="15">MERROW</text>
      <text class="seal-name" x="297" y="768" font-size="15">DALTON</text>
      <text class="head" x="297" y="850" font-size="42">MERROW DALTON</text>
      <text class="head" x="297" y="877" font-size="25">APOTHECARY</text>
      <rect class="cream" x="152" y="890" width="290" height="102"/>
      <rect class="frame-ink" x="164" y="905" width="266" height="73"/>
      <rect class="cream" x="236" y="893" width="122" height="22"/>
      <text class="serif-ink" x="297" y="911" font-size="22" letter-spacing="1">SOFTENING</text>
      <text class="head-ink" x="297" y="970" font-size="68">BEARD OIL</text>
      <text class="cond" x="297" y="1024" font-size="22">STRENGTHEN AND CONDITION</text>
      <text class="cond" x="297" y="1046" font-size="13">YOUR BEARD WITH THIS BLEND OF NATURAL OILS</text>
      <line x1="198" y1="1060" x2="398" y2="1060" stroke="#fff" stroke-width="2"/>
      <g role="img" aria-label="Fine gold contour-line pattern">
        <rect x="152" y="1122" width="290" height="112" fill="url(#gold-wash)"/>
      </g>
      <text class="cond" x="297" y="1088" font-size="19">SUNFLOWER OIL &amp; AVOCADO OIL</text>
      <text class="cond" x="297" y="1115" font-size="24">VITAMINS E, C, B, AND A</text>
      <text class="cond" x="297" y="1148" font-size="20">• BEST OIL FOR GENTLEMEN •</text>
      <rect class="gold-band" x="163" y="1163" width="268" height="48"/>
      <text class="head" x="297" y="1203" font-size="46">TIMBER VAULT</text>
      <text class="volume" x="297" y="1261" font-size="15">60 ml / 2 fl oz</text>
    </g>
  </defs>

  <!-- ============ CARTON ============ -->
  <g class="carton">
    <!-- hanger / closure panel with die-cut hole -->
    <rect class="panel" x="121" y="126" width="353" height="546"/>
    <line class="fold" x1="121" y1="277" x2="474" y2="277"/>
    <line class="fold" x1="121" y1="521" x2="474" y2="521"/>
    <line class="fold" x1="121" y1="400" x2="202" y2="400"/>
    <circle cx="298" cy="400" r="96" fill="#fff"/>
    <rect x="121" y="126" width="353" height="546" fill="none" stroke="var(--rule)" stroke-width="3"/>

    <!-- dust flaps -->
    <path class="panel" d="M478 672 L490 660 L515 535 L698 535 L698 640 L725 672 Z"/>
    <path class="panel" d="M1078 672 L1104 640 L1104 535 L1285 535 L1310 660 L1330 672 Z"/>
    <path class="panel" d="M474 1278 L490 1300 L512 1418 L698 1418 L698 1308 L725 1278 Z"/>
    <path class="panel" d="M1078 1278 L1104 1308 L1104 1418 L1285 1418 L1310 1300 L1330 1278 Z"/>

    <!-- top tuck flap -->
    <path class="panel" d="M725 672 L725 420 Q725 372 773 372 L1030 372 Q1078 372 1078 420 L1078 672 Z"/>
    <path class="fold" d="M725 470 L785 470 L785 488 L1020 488 L1020 470 L1078 470"/>
    <circle class="brand-seal" cx="902" cy="578" r="68"/>
    <text class="seal-name" x="902" y="574" font-size="16">MERROW</text>
    <text class="seal-name" x="902" y="595" font-size="16">DALTON</text>

    <!-- bottom tuck flap -->
    <path class="panel" d="M725 1278 L725 1528 Q725 1576 773 1576 L1030 1576 Q1078 1576 1078 1528 L1078 1278 Z"/>
    <path class="fold" d="M785 1460 L1020 1460 L1020 1478 L1078 1478"/>

    <!-- glue flap -->
    <path class="panel" d="M1330 672 L1406 690 L1406 1262 L1330 1278 Z"/>

    <!-- main body -->
    <rect class="panel" x="121" y="672" width="1209" height="606"/>
    <line class="fold" x1="474" y1="672" x2="474" y2="1278"/>
    <line class="fold" x1="725" y1="672" x2="725" y2="1278"/>
    <line class="fold" x1="1078" y1="672" x2="1078" y2="1278"/>
    <line class="fold" x1="1330" y1="672" x2="1330" y2="1278"/>
    <line class="fold" x1="121" y1="672" x2="1330" y2="672"/>
    <line class="fold" x1="121" y1="1278" x2="1330" y2="1278"/>

    <!-- front faces -->
    <use href="#front-face"/>
    <use href="#front-face" transform="translate(605 0)"/>

    <!-- side panel: ingredients -->
    <g class="side-ingredients">
      <text class="head" x="600" y="718" font-size="36">MERROW DALTON</text>
      <text class="head" x="600" y="741" font-size="22">APOTHECARY</text>
      <rect class="frame" x="496" y="753" width="207" height="502"/>
      <rect class="frame-dash" x="512" y="768" width="176" height="472"/>
      <g role="img" aria-label="Barber emblem with moustache, crossed razors and 'The Best' script">
        <rect x="538" y="780" width="124" height="112" rx="8" fill="#2a2a2a"/>
      </g>
      <line class="dots" x1="540" y1="905" x2="662" y2="905"/>
      <text class="head" x="600" y="938" font-size="24">STRENGTHEN</text>
      <text class="head" x="600" y="963" font-size="24">AND</text>
      <text class="head" x="600" y="989" font-size="24">CONDITION</text>
      <line class="dots" x1="540" y1="1005" x2="662" y2="1005"/>
      <text class="serif" x="600" y="1030" font-size="14">your beard with this</text>
      <text class="serif" x="600" y="1045" font-size="14">blend of natural</text>
      <rect class="cream" x="498" y="1061" width="203" height="19"/>
      <text class="serif-ink" x="600" y="1076" font-size="17">Sunflower oil</text>
      <text class="serif" x="600" y="1103" font-size="12">Is rich in Omega, fatty acids</text>
      <text class="serif" x="600" y="1117" font-size="12">and vitamins E, C, B and A</text>
      <rect class="cream" x="498" y="1131" width="203" height="19"/>
      <text class="serif-ink" x="600" y="1146" font-size="17">Avocado oil</text>
      <text class="serif" x="600" y="1176" font-size="14">Hydtates the beard fibers</text>
      <text class="serif" x="600" y="1191" font-size="14">from root to tip</text>
      <g role="img" aria-label="Moustache icon">
        <rect x="578" y="1210" width="46" height="14" rx="7" fill="#fff"/>
      </g>
    </g>

    <!-- side panel: description -->
    <g class="side-description">
      <rect class="frame" x="1101" y="752" width="208" height="503"/>
      <rect class="frame-dash" x="1118" y="767" width="175" height="473"/>
      <circle class="brand-seal" cx="1206" cy="755" r="62"/>
      <text class="seal-name" x="1206" y="751" font-size="15">MERROW</text>
      <text class="seal-name" x="1206" y="771" font-size="15">DALTON</text>
      <text class="head" x="1206" y="858" font-size="32">MERROW DALTON</text>
      <text class="head" x="1206" y="879" font-size="21">APOTHECARY</text>
      <text class="head" x="1206" y="929" font-size="52">BEARD OIL</text>
      <line class="dots" x1="1148" y1="945" x2="1264" y2="945"/>
      <text class="serif" x="1206" y="970" font-size="16">Keep the beard looking</text>
      <text class="serif" x="1206" y="988" font-size="16">and feeling extraordinary.</text>
      <text class="serif" x="1206" y="1006" font-size="16">Smooth into your beard</text>
      <text class="serif" x="1206" y="1024" font-size="16">for a healthy sheen and</text>
      <text class="serif" x="1206" y="1042" font-size="16">a woodsy scent evoking</text>
      <text class="serif" x="1206" y="1060" font-size="16">the great outdoors.</text>
      <line class="dots" x1="1148" y1="1075" x2="1264" y2="1075"/>
      <text class="serif" x="1206" y="1099" font-size="11.5">Direction: Apply a small amount</text>
      <text class="serif" x="1206" y="1117" font-size="11.5">in your palm. Gently massage into</text>
      <text class="serif" x="1206" y="1135" font-size="11.5">the beard hair and underneath skin.</text>
      <g role="img" aria-label="Crossed scissors and straight razor">
        <rect x="1162" y="1150" width="86" height="76" rx="6" fill="#2a2a2a"/>
      </g>
    </g>
  </g>

  <!-- carton dimensions -->
  <g class="dimensions">
    <path class="dim-line" d="M127 97 H1403 M127 80 V115 M1403 80 V115"/>
    <text class="dim-text" x="765" y="75">30 cm</text>
    <path class="dim-line" d="M70 684 V1274 M52 684 H90 M52 1274 H90"/>
    <text class="dim-text" transform="translate(50 968) rotate(-90)">12 cm</text>
    <path class="dim-line" d="M121 1347 H465 M121 1330 V1365 M465 1330 V1365"/>
    <text class="dim-text" x="310" y="1387">7 cm</text>
    <path class="dim-line" d="M489 1465 H696 M489 1447 V1483 M696 1447 V1483"/>
    <text class="dim-text" x="598" y="1507">4  cm</text>
    <path class="dim-line" d="M1468 143 V1576 M1450 143 H1487 M1450 1576 H1487"/>
    <text class="dim-text" transform="translate(1490 812) rotate(90)">26.8 cm</text>
  </g>

  <!-- ============ BOTTLE LABEL ============ -->
  <g class="label">
    <rect class="panel" x="1538" y="630" width="640" height="320" rx="40"/>

    <!-- label front -->
    <rect class="frame" x="1580" y="690" width="215" height="238"/>
    <circle class="brand-seal" cx="1688" cy="692" r="50"/>
    <text class="seal-name" x="1688" y="689" font-size="12">MERROW</text>
    <text class="seal-name" x="1688" y="705" font-size="12">DALTON</text>
    <text class="head" x="1688" y="764" font-size="21">MERROW DALTON</text>
    <text class="head" x="1688" y="776" font-size="11">APOTHECARY</text>
    <rect class="cream" x="1582" y="783" width="211" height="85"/>
    <rect class="frame-ink" x="1592" y="795" width="191" height="60" stroke-width="2.5"/>
    <rect class="cream" x="1638" y="789" width="98" height="14"/>
    <text class="serif-ink" x="1687" y="801" font-size="15" letter-spacing="1">SOFTENING</text>
    <text class="head-ink" x="1687" y="848" font-size="48">BEARD OIL</text>
    <text class="cond" x="1646" y="882" font-size="10">STRENGTHEN AND CONDITION</text>
    <text class="cond" x="1646" y="892" font-size="5.5">YOUR BEARD WITH THIS BLEND OF NATURAL OILS</text>
    <text class="cond" x="1646" y="903" font-size="6.5">SUNFLOWER OIL &amp; AVOCADO OIL</text>
    <text class="cond" x="1646" y="919" font-size="13">VITAMINS E, C, B, AND A</text>
    <line x1="1712" y1="868" x2="1712" y2="928" stroke="#fff" stroke-width="2"/>
    <g role="img" aria-label="Wavy line texture">
      <rect x="1714" y="870" width="79" height="56" fill="url(#stripe-wash)"/>
    </g>
    <text class="head" x="1765" y="894" font-size="26">SALT</text>
    <text class="head" x="1753" y="919" font-size="26">DRIFT</text>
    <text class="volume" x="1686" y="945" font-size="10">60 ml / 2 fl oz</text>

    <!-- label back -->
    <rect class="frame" x="1922" y="672" width="214" height="256"/>
    <circle class="brand-seal" cx="2028" cy="672" r="32"/>
    <text class="seal-name" x="2028" y="670" font-size="8">MERROW</text>
    <text class="seal-name" x="2028" y="680" font-size="8">DALTON</text>
    <text class="serif" x="2028" y="723" font-size="11" letter-spacing="0.6">Keep the beard looking and feeling</text>
    <text class="serif" x="2028" y="736" font-size="11" letter-spacing="0.6">extraordinary. Smooth into your</text>
    <text class="serif" x="2028" y="749" font-size="11">beard for a healthy sheen and a woodsy</text>
    <text class="serif" x="2028" y="762" font-size="11">scent evoking the great outdoors.</text>
    <text class="serif-left" x="1940" y="786" font-size="11">Sunflower oil</text>
    <text class="serif-left" x="1940" y="801" font-size="11">Is rich in Omega, fatty acids and</text>
    <text class="serif-left" x="1940" y="813" font-size="11">vitamins E, C, B and A</text>
    <text class="serif-left" x="1940" y="831" font-size="11">Avocado oil</text>
    <text class="serif-left" x="1940" y="846" font-size="11">Hydtates the beard fibers from root to tip</text>
    <text class="serif-left" x="1940" y="867" font-size="11">Direction: Apply a small amount in</text>
    <text class="serif-left" x="1940" y="880" font-size="11">your palm. Gently massage into the beard</text>
    <text class="serif-left" x="1940" y="892" font-size="11">hair and underneath skin.</text>
    <g role="img" aria-label="Moustache icon">
      <rect x="2013" y="906" width="32" height="9" rx="4.5" fill="#fff"/>
    </g>
  </g>

  <!-- label dimensions and note -->
  <g class="dimensions">
    <path class="dim-line" d="M1580 600 H2147 M1580 583 V618 M2147 583 V618"/>
    <text class="dim-text" x="1857" y="572">12 cm</text>
    <path class="dim-line" d="M2208 637 V952 M2190 637 H2227 M2190 952 H2227"/>
    <text class="dim-text" transform="translate(2220 794) rotate(90)">6 cm</text>
    <path class="dim-line" d="M1584 993 H1787 M1584 975 V1011 M1787 975 V1011"/>
    <text class="dim-text" x="1693" y="984">4 cm</text>
    <path class="dim-line" d="M1795 993 H1912 M1795 975 V1011 M1912 975 V1011"/>
    <text class="dim-text" x="1855" y="984">3 cm</text>
    <path class="dim-line" d="M1922 993 H2135 M1922 975 V1011 M2135 975 V1011"/>
    <text class="dim-text" x="2031" y="984">4 cm</text>
    <text class="note" x="1580" y="1117">*The size of label could be chage depends</text>
    <text class="note" x="1580" y="1156">on the real dimention of the bottle.</text>
  </g>
</svg>
</body>
</html>
```